Need Letterhead Design & Matching Business Card

I have a logo that I love already. But the letterhead is less than appealing and boring. I'd like a design for my letterhead which I will match with business cards. Also, I'd like to have used fonts that are generally available, as my current letterhead uses a font named "SPACE" which nobody has unless they download it...so when a Word version is forwarded, it looks awful on the receiver's screed due to not having the font. That being said, modern is the look we like and are going for.

My business is "Halloran Brightmoor PC" - a law firm specializing in representing people who have suffered catastrophic injuries or death (plane, auto, train crashes etc.).

See attached letterhead, which has all of the pertinent information. My logo is also attached in various formats.

```html
<!DOCTYPE html>
<html lang="en">
<head>
<meta charset="utf-8">
<title>Halloran Brightmoor PC — Stationery</title>
<link rel="stylesheet" href="https://fonts.googleapis.com/css2?family=Josefin+Sans:wght@300;400&display=swap">
<style>
  :root {
    --ink: #1a1a1a;
    --paper: #ffffff;
    --muted: #6a6a6a;
    --rule: #cfcfcf;
    --faint: #f2f2f2;
    --shadow: rgba(0, 0, 0, 0.14);
  }
  * { box-sizing: border-box; margin: 0; padding: 0; }
  html, body { width: 771px; height: 1200px; overflow: hidden; background: var(--paper); }
  body { position: relative; font-family: "Josefin Sans", sans-serif; font-weight: 300; color: var(--ink); }

  .brand { position: absolute; display: flex; align-items: center; }
  .brand-square { background: var(--ink); flex: none; }
  .brand-name { display: flex; flex-direction: column; text-transform: uppercase; font-weight: 300; line-height: 1; }
  .brand-name .line-1 { letter-spacing: 0.04em; }
  .brand-name .line-2 { letter-spacing: 0.3em; }

  /* Hero lockup */
  .hero { left: 100px; top: 70px; gap: 22px; }
  .hero .brand-square { width: 78px; height: 78px; }
  .hero .line-1 { font-size: 66px; }
  .hero .line-2 { font-size: 27px; margin-top: 8px; }

  /* Business cards */
  .card { position: absolute; top: 272px; width: 344px; height: 194px; box-shadow: 0 1px 5px var(--shadow); overflow: hidden; }
  .card-front { left: 30px; background: var(--paper); }
  .card-back { left: 388px; background: var(--ink); }
  .card-bar { position: absolute; height: 10px; background: var(--ink); }
  .card-bar.top { left: 0; top: 0; width: 160px; }
  .card-bar.bottom { right: 0; bottom: 0; width: 160px; }

  .card-front .brand { left: 16px; top: 82px; gap: 7px; }
  .card-front .brand-square { width: 24px; height: 24px; }
  .card-front .line-1 { font-size: 15px; }
  .card-front .line-2 { font-size: 6.5px; margin-top: 3px; }

  .card-divider { position: absolute; left: 170px; top: 68px; width: 1px; height: 58px; background: var(--rule); }
  .card-contacts { position: absolute; left: 182px; top: 68px; list-style: none; font-size: 7.5px; color: var(--muted); font-weight: 400; }
  .card-contacts li { display: flex; align-items: center; gap: 6px; height: 14.5px; }
  .card-contacts svg { width: 8px; height: 8px; flex: none; }

  .card-back .brand { left: 50%; top: 50%; transform: translate(-50%, -50%); gap: 9px; color: var(--paper); }
  .card-back .brand-square { width: 30px; height: 30px; background: var(--paper); }
  .card-back .line-1 { font-size: 19px; }
  .card-back .line-2 { font-size: 8px; margin-top: 4px; }

  /* Letterhead */
  .letterhead { position: absolute; left: 176px; top: 534px; width: 418px; height: 614px; background: var(--paper); box-shadow: 0 1px 6px var(--shadow); }
  .letterhead .brand { left: 16px; top: 38px; gap: 10px; }
  .letterhead .brand-square { width: 44px; height: 44px; }
  .letterhead .line-1 { font-size: 35px; }
  .letterhead .line-2 { font-size: 14px; margin-top: 5px; }
  .letterhead-mark { position: absolute; left: 135px; top: 215px; width: 150px; height: 150px; background: var(--faint); }
  .letterhead-footer { position: absolute; bottom: 24px; font-size: 6.5px; line-height: 1.5; color: var(--muted); font-weight: 400; }
  .letterhead-footer.address { left: 16px; }
  .letterhead-footer.contact { left: 282px; }
</style>
</head>
<body>

  <div class="brand hero">
    <div class="brand-square"></div>
    <div class="brand-name"><span class="line-1">Halloran</span><span class="line-2">Brightmoor PC</span></div>
  </div>

  <section class="card card-front">
    <div class="card-bar top"></div>
    <div class="brand">
      <div class="brand-square"></div>
      <div class="brand-name"><span class="line-1">Halloran</span><span class="line-2">Brightmoor PC</span></div>
    </div>
    <div class="card-divider"></div>
    <ul class="card-contacts">
      <li><svg viewBox="0 0 8 8"><circle cx="4" cy="4" r="4" fill="#333"/></svg>law@halloranbrightmoor.com</li>
      <li><svg viewBox="0 0 8 8"><circle cx="4" cy="4" r="4" fill="#333"/></svg>(800) 555-0142</li>
      <li><svg viewBox="0 0 8 8"><circle cx="4" cy="4" r="4" fill="#333"/></svg>www.halloranbrightmoor.com</li>
      <li><svg viewBox="0 0 8 8"><circle cx="4" cy="4" r="4" fill="#333"/></svg>410 Crestline Ave, Suite 200</li>
    </ul>
    <div class="card-bar bottom"></div>
  </section>

  <section class="card card-back">
    <div class="brand">
      <div class="brand-square"></div>
      <div class="brand-name"><span class="line-1">Halloran</span><span class="line-2">Brightmoor PC</span></div>
    </div>
  </section>

  <section class="letterhead">
    <div class="brand">
      <div class="brand-square"></div>
      <div class="brand-name"><span class="line-1">Halloran</span><span class="line-2">Brightmoor PC</span></div>
    </div>
    <div class="letterhead-mark"></div>
    <div class="letterhead-footer address">
      410 Crestline Avenue, Floor 3<br>
      Suite 200, Marlow Park<br>
      CA 90411
    </div>
    <div class="letterhead-footer contact">
      law@halloranbrightmoor.com<br>
      www.halloranbrightmoor.com<br>
      tel. (800) 555-0142
    </div>
  </section>

</body>
</html>
```